Managed Service Provider need new business cards

We are a small Maanged Service Provider of IT Services and need a new fresh design for our business cards. We want something impossible, fun and professional :)
Our services has a large range, but we are always fun and make sure our customers both get their issue sorted and also feel like they are "catching up with an old friend".
All our cards in the past has always been all black, with red and we need something fresher.
The back of card, we would like just a small list of what we do i think, but if someone has a better idea, please do something cool with the back of the card:
Managed IT Services
Productivity Solutions
Data Backup and Recovery
IT System Maintenance
Managed IT Security
More details can be found on our website tqnetworks.com.au
Industry/Entity Type
It Company
Contact Information for Business Card
Name: Dwayne Falstrup
Title: Director
Phone: 03 6193 4827
Mobile: 0412 587 239
Email: dwayne@tqnetworks.com.au
Web: www.tqnetworks.com.au

```html
<!DOCTYPE html>
<html lang="en">
<head>
<meta charset="utf-8">
<title>TQ Networks – Business Cards</title>
<link href="https://fonts.googleapis.com/css2?family=Lato:wght@400;700;900&display=swap" rel="stylesheet">
<style>
  :root {
    --bg: #3a3430;
    --card: #18181b;
    --red: #e3141c;
    --white: #f4f4f4;
    --divider: #8a1014;
  }
  * { box-sizing: border-box; margin: 0; padding: 0; }
  html, body { width: 1200px; height: 847px; overflow: hidden; }
  body {
    background: var(--bg);
    font-family: "Lato", sans-serif;
    position: relative;
  }
  .card {
    position: absolute;
    top: 258px;
    width: 540px;
    height: 330px;
    background: var(--card);
    border-bottom: 4px solid var(--red);
    border-right: 2px solid var(--red);
    box-shadow: 0 14px 30px rgba(0,0,0,0.45);
    display: flex;
    align-items: center;
  }
  .card--back { left: 40px; }
  .card--front { left: 620px; }

  .brand {
    width: 250px;
    display: flex;
    align-items: center;
    justify-content: center;
    gap: 10px;
  }
  .brand__dot {
    width: 14px; height: 14px;
    border-radius: 50%;
    background: var(--red);
  }
  .brand__name {
    color: var(--red);
    font-weight: 900;
    font-size: 30px;
    letter-spacing: 0.5px;
  }

  .divider {
    width: 1px;
    height: 150px;
    background: var(--divider);
  }

  .services {
    list-style: none;
    padding-left: 30px;
    color: var(--white);
    font-size: 16px;
    line-height: 27px;
  }
  .services li { display: flex; align-items: center; gap: 12px; }
  .services li::before {
    content: "";
    width: 6px; height: 6px;
    border-radius: 50%;
    background: var(--red);
  }

  .contact { padding-left: 26px; color: var(--white); }
  .contact__name {
    color: var(--red);
    font-weight: 700;
    font-size: 26px;
    line-height: 1.1;
  }
  .contact__title { font-size: 15px; margin-bottom: 14px; }
  .contact__list { list-style: none; font-size: 15px; line-height: 25px; }
  .contact__list li { display: flex; align-items: center; gap: 10px; }
  .contact__list svg { width: 14px; height: 14px; flex: none; }
  .contact__accent { color: var(--red); }
</style>
</head>
<body>

<section class="card card--back" aria-label="Card back">
  <div class="brand">
    <span class="brand__dot"></span>
    <span class="brand__name">TQ Networks</span>
  </div>
  <div class="divider"></div>
  <ul class="services">
    <li>Managed IT Services</li>
    <li>Productivity Solutions</li>
    <li>Data Backup and Recovery</li>
    <li>IT System Maintenance</li>
    <li>Managed IT Security</li>
  </ul>
</section>

<section class="card card--front" aria-label="Card front">
  <div class="brand">
    <span class="brand__dot"></span>
    <span class="brand__name">TQ Networks</span>
  </div>
  <div class="divider"></div>
  <div class="contact">
    <p class="contact__name">Dwayne Falstrup</p>
    <p class="contact__title">Director</p>
    <ul class="contact__list">
      <li>
        <svg viewBox="0 0 16 16" aria-hidden="true"><path fill="#e3141c" d="M3 1l3 3-1.5 2a9 9 0 0 0 5.5 5.5L12 10l3 3-2 2C6 15 1 10 1 3z"/></svg>
        03 6193 4827
      </li>
      <li>
        <svg viewBox="0 0 16 16" aria-hidden="true"><rect x="4" y="1" width="8" height="14" rx="1.5" fill="none" stroke="#e3141c" stroke-width="1.6"/><circle cx="8" cy="12.3" r="0.9" fill="#e3141c"/></svg>
        0412 587 239
      </li>
      <li>
        <svg viewBox="0 0 16 16" aria-hidden="true"><rect x="1" y="3" width="14" height="10" fill="#e3141c"/><path d="M1 3l7 6 7-6M1 13l5-5M15 13l-5-5" fill="none" stroke="#18181b" stroke-width="1.2"/></svg>
        dwayne@tqnetworks.com.au
      </li>
      <li>
        <svg viewBox="0 0 16 16" aria-hidden="true"><g fill="none" stroke="#e3141c" stroke-width="1.3"><circle cx="8" cy="8" r="6.5"/><ellipse cx="8" cy="8" rx="3" ry="6.5"/><path d="M1.5 8h13M3 4.5h10M3 11.5h10"/></g></svg>
        <span>www.<span class="contact__accent">tqnetworks</span>.com.au</span>
      </li>
    </ul>
  </div>
</section>

</body>
</html>
```